Visit card

Industry/Entity Type

Health Care

Contact Information for Business Card

O VITAL SYSTEMIQUE
Odile Ferrand - chef de Projet

Requirements
Must have
• 318 Rue des Tilleuls Verts 47150 VAUVERLIN Tel: 33 (0) 487 204 615 Mobile: 06 42 93 17 58 Web: www.cliniqorvane.example Contact: o.ferrand@o-vitalsystemique.example
Should not have
• Respect for color

```html
<!DOCTYPE html>
<html lang="fr">
<head>
<meta charset="utf-8">
<title>O Vital Systemique – Carte de visite</title>
<link href="https://fonts.googleapis.com/css2?family=Open+Sans:wght@400;600;800&display=swap" rel="stylesheet">
<style>
  :root {
    --backdrop: #272727;
    --paper: #ffffff;
    --brand-red: #e8232e;
    --charcoal: #404041;
    --card-dark: #4a4a4a;
    --card-mid: #5b5b5b;
    --card-light: #a9a6a5;
    --text-light: #ffffff;
  }
  * { margin: 0; padding: 0; box-sizing: border-box; }
  html, body {
    width: 1200px; height: 1200px; overflow: hidden;
    background: var(--backdrop);
    font-family: "Open Sans", Arial, sans-serif;
  }
  .canvas { position: relative; width: 1200px; height: 1200px; }

  .card {
    position: absolute; left: 254px; width: 665px; height: 408px;
    overflow: hidden;
    box-shadow: 0 2px 6px rgba(0,0,0,.45);
  }
  .card--front { top: 116px; background: var(--paper); }
  .card--back {
    top: 638px;
    background:
      radial-gradient(ellipse 320px 300px at 100px 185px, rgba(40,40,40,.55), transparent 70%),
      linear-gradient(180deg, var(--card-light) 0%, var(--card-mid) 22%, var(--card-dark) 60%, var(--card-dark) 100%);
  }
  .card--back::after {
    content: ""; position: absolute; inset: 0;
    background: radial-gradient(ellipse 260px 160px at 0 100%, rgba(200,197,196,.55), transparent 70%);
    pointer-events: none;
  }

  .brand {
    position: absolute; inset: 0;
    display: flex; align-items: center; justify-content: center; gap: 22px;
  }
  .brand__dot { width: 46px; height: 46px; border-radius: 50%; background: var(--brand-red); }
  .brand__name {
    font-weight: 600; font-size: 34px; letter-spacing: 2px;
    color: var(--charcoal);
  }

  .backdrop-disc {
    position: absolute; left: -150px; top: 45px; width: 390px; height: 390px;
    border-radius: 50%; background: #3f3f3f; opacity: .55;
    box-shadow: 0 0 40px rgba(0,0,0,.4);
  }

  .name-band {
    position: absolute; left: 326px; right: 0; top: 79px; height: 78px;
    background: linear-gradient(90deg, rgba(232,35,46,0) 0%, var(--brand-red) 32%, var(--brand-red) 100%);
  }
  .contact-block {
    position: absolute; right: 53px; top: 86px; z-index: 1;
    text-align: right; color: var(--text-light);
  }
  .contact-block__name { font-weight: 800; font-size: 25px; line-height: 32px; }
  .contact-block__role { font-weight: 400; font-size: 25px; line-height: 32px; }
  .contact-block__address {
    margin-top: 32px; font-size: 22px; line-height: 27px;
  }
  .contact-block__web {
    margin-top: 16px; font-size: 22px; line-height: 27px;
    font-weight: 800; color: var(--brand-red);
  }
  .contact-block__email { font-size: 22px; line-height: 27px; }
</style>
</head>
<body>
<main class="canvas">
  <section class="card card--front">
    <div class="brand">
      <span class="brand__dot"></span>
      <span class="brand__name">O VITAL SYSTEMIQUE</span>
    </div>
  </section>

  <section class="card card--back">
    <div class="backdrop-disc"></div>
    <div class="name-band"></div>
    <div class="contact-block">
      <p class="contact-block__name">Odile FERRAND</p>
      <p class="contact-block__role">Chef de Projet</p>
      <p class="contact-block__address">
        318 Rue des Tilleuls Verts<br>
        47150 VAUVERLIN<br>
        Tél : +33 (0) 487 204 615<br>
        Mobil : 06 42 93 17 58
      </p>
      <p class="contact-block__web">www.cliniqorvane.example</p>
      <p class="contact-block__email">o.ferrand@o-vitalsystemique.example</p>
    </div>
  </section>
</main>
</body>
</html>
```